Larkhollow Fitness

Personal training company specializing in fat burn and toning in minimal time with maximal results.

I am looking to launch my company and i am looking to target a specific market women between the ages of 30 to 50 who are stay at home mums and business professionals looking to kick start there health and fitness goals. We are based in the Epsom Ewell area in Surrey. Our initial product are the 30 minute 1to1 sessions. Colors of my company brand are cyan and black. The final design should communicate "solid results minimal time" and should have a tear off tab so i can capture data.

Target Market(s)

women between 30-50 yrs old stay at home mums or buisness proffesionals

Industry/Entity Type

Training

Requirements
Must have
• Tear off section to capture details of potential clients
Should not have
• no money bags
no cheesey sayings

```html
<!DOCTYPE html>
<html lang="en">
<head>
<meta charset="utf-8">
<title>Larkhollow Fitness – KICKSTART Program</title>
<link rel="stylesheet" href="https://fonts.googleapis.com/css2?family=Alegreya:wght@500;700&family=Merriweather:wght@400;700;900&family=Roboto+Condensed:wght@400&family=Noto+Serif:wght@400&display=swap">
<style>
  :root {
    --blue-deep: #1c56c9;
    --blue-mid: #2f74e0;
    --blue-light: #5a9af0;
    --white: #ffffff;
    --ink: #161616;
    --band: #0d0d0d;
    --accent-blue: #2b6fd8;
  }
  * { margin: 0; padding: 0; box-sizing: border-box; }
  html, body { width: 1200px; height: 924px; overflow: hidden; }
  body {
    position: relative;
    background: radial-gradient(ellipse at 55% 35%, var(--blue-light) 0%, var(--blue-mid) 45%, var(--blue-deep) 100%);
    color: var(--white);
    font-family: "Alegreya", serif;
  }
  .shapes { position: absolute; inset: 0; }
  .headline {
    position: absolute; left: 34px; top: 36px;
    font-family: "Alegreya", serif; font-weight: 700;
    color: var(--ink); font-size: 38px; line-height: 40px;
    letter-spacing: -0.2px;
    transform: scaleX(1.07); transform-origin: left top;
    white-space: nowrap;
  }
  .headline .members { display: flex; align-items: center; }
  .avatar {
    display: inline-block; width: 32px; height: 38px; margin-left: 10px;
    background: linear-gradient(#c9c3bb, #6d6a66); border: 1px solid #999;
  }
  .avatar:first-of-type { margin-left: 36px; }
  .avatar:last-of-type { margin-right: 30px; }
  .question {
    position: absolute; left: 26px; top: 206px;
    font-family: "Roboto Condensed", sans-serif; font-size: 29.5px; color: var(--white);
    white-space: nowrap;
  }
  .salutation {
    position: absolute; left: 36px; top: 272px;
    font-family: "Merriweather", serif; font-weight: 900; font-size: 31px; letter-spacing: 1.6px;
    white-space: nowrap;
  }
  .letter {
    position: absolute; left: 37px; top: 317px;
    font-weight: 700; font-size: 34px; line-height: 41.5px; letter-spacing: -0.4px;
    transform: scaleX(0.9); transform-origin: left top;
    white-space: nowrap;
  }
  .letter u { text-underline-offset: 4px; }
  .includes-title {
    position: absolute; left: 46px; top: 636px;
    font-family: "Merriweather", serif; font-weight: 700; font-size: 33px; letter-spacing: 0.8px;
    color: var(--ink); white-space: nowrap;
  }
  .includes {
    position: absolute; left: 48px; top: 687px; list-style: none;
    font-family: "Noto Serif", serif; font-size: 16.5px; color: var(--ink); line-height: 18px;
    white-space: nowrap;
  }
  .includes li { margin-bottom: 17px; }
  .includes li::before { content: "· "; }
  .includes .cont { padding-left: 8px; display: block; }
  .hero-photo {
    position: absolute; left: 900px; top: 472px; width: 280px; height: 452px;
    background: linear-gradient(180deg, rgba(60,40,35,0.55), rgba(210,160,130,0.6) 45%, rgba(25,25,25,0.8));
    border-radius: 110px 110px 10px 10px;
  }
  .tear-off {
    position: absolute; top: 862px; left: 0; width: 880px; height: 40px;
    font-family: "Merriweather", serif; font-size: 24px; color: var(--accent-blue);
    white-space: nowrap;
  }
  .tear-off span { position: absolute; top: 0; }
  .tear-off .label { left: 22px; font-weight: 700; letter-spacing: 0.6px; }
  .tear-off .field-name { left: 249px; }
  .tear-off .field-phone { left: 489px; }
</style>
</head>
<body>
  <svg class="shapes" width="1200" height="924" viewBox="0 0 1200 924" aria-hidden="true">
    <polygon points="0,34 1094,34 1024,168 0,168" fill="#0a0a0a" transform="translate(6,4)"/>
    <polygon points="0,30 1090,30 1020,164 0,164" fill="#ffffff"/>
    <polygon points="22,196 1188,196 1160,260 0,262 0,230" fill="#0d0d0d"/>
    <polygon points="0,840 880,840 855,924 0,924" fill="#ffffff"/>
    <line x1="0" y1="840" x2="880" y2="840" stroke="#111" stroke-width="2" stroke-dasharray="5 4"/>
    <g transform="translate(668,812)" stroke="#111" stroke-width="2.5" fill="none">
      <circle cx="20" cy="6" r="5"/>
      <circle cx="24" cy="22" r="5"/>
      <line x1="0" y1="14" x2="17" y2="10"/>
      <line x1="0" y1="16" x2="20" y2="19"/>
    </g>
  </svg>

  <div class="headline">
    <div>Who Else Wants to Lose At LEAST 15 Pounds Fast…</div>
    <div>And Look And Feel Better Than You Have In Years?</div>
    <div class="members">These Members Did…
      <span class="avatar" role="img" aria-label="Member portrait"></span>
      <span class="avatar" role="img" aria-label="Member portrait"></span>
      <span class="avatar" role="img" aria-label="Member portrait"></span>
      And Now You Can Too!</div>
  </div>

  <div class="question">Why do some Members succeed with their fitness and weight loss goals while others struggle?</div>

  <div class="salutation">Dear Perspective Clients,</div>
  <div class="letter">
    We know the answer, and now you can discover the <u>proven &amp; guaranteed</u> system<br>
    that’s helped so many of our Members reach their fitness goals and look<br>
    and feel better than ever…in the shortest period of time possible.<br>
    Just accept our £61.00 gift (while it lasts) and get started the right way,<br>
    right now by calling 07700 900418 (or bring this card to the front<br>
    desk and ask for Mark) to join our Custom KICKSTART Program…<br>
    a £325.00 Value for ONLY £260.00! (Save £61.00)
  </div>

  <div class="includes-title">Your KICKSTART Program Includes:</div>
  <ul class="includes">
    <li>16 30min Fat-Blasting Training Session with a<span class="cont">Larkhollow Fitness Professional (£347.00 Value)</span></li>
    <li>4 Weeks of Nutritional Guidance &nbsp;(£32 Value)</li>
    <li>Unlimited E-mail Coaching (Priceless)</li>
    <li>Done-For-You Meal Plan (£57 Value)</li>
  </ul>

  <div class="hero-photo" role="img" aria-label="Smiling woman in workout wear with a towel around her neck giving a thumbs up"></div>

  <div class="tear-off">
    <span class="label">Client info :</span>
    <span class="field-name">Name__________</span>
    <span class="field-phone">Phone___________</span>
  </div>
</body>
</html>
```